IT Services Business Card Design

We require a business card design for an IT services company called RT Code Transit.

We specialize in taking an organisations software and readying it for deployment to new environments (e.g. Nex 3 to Nex 5). This process is termed application packaging. This is not the same as putting things in boxes but I am happy to use boxes as a pun icon ;-) This is our second step in branding, we currently have a new logo and our poor excuse of a website is next to be updated but it contains information on who we are and what we cover at rtcodetransit.example

We are looking for a fun, modern but stylish and professional looking design.

I have attached the logo in multiple formats including vector formats (and the fonts that created the logo if required)
Updates

Thanks to all the designers so far, some great designs in there.  I will be selecting a card design on the deadline date. 

However, there is still time to submit some more designs.  The majority of the ones I have so far are typical simplistic designs that we have all seen before and I have enough of those to choose from now.  If you wish to submit any more designs, please submit somthing unusual to grab our attention.

Target Market(s)

Project executives of large organisations looking for Nexora migrations

Industry/Entity Type

Software

Requirements
Must have
• Want to show company name, contact name, title, main number, contact number, fax number, email address and website address. I do not want to show the address.
Must use the attached logo, retaining the colours in them.

This has to be a double-sided design. I will be using pelby.example and will be selecting their rounded corner business card design.

Their templates and design requirements (sizing etc.) can be found here: http://uk.pelby.example/help/faq/templates-and-guidelines.html

Happy for company name or website to be on either side of the card.

This design has to be original and not used before for another company

Would like to style it around the business colours in the logo
Nice to have
• Pelby.example has an option for multiple card designs to appear on the back. If this is possible in the budget and time you have and you have a design(s) that work with that but carry the same style and theme, that would be nice to see but not necessary.
Should not have
• We do not want to put a postal address on the cards

```html
<!DOCTYPE html>
<html lang="en">
<head>
<meta charset="utf-8">
<title>RT Code Transit – Business Card</title>
<link href="https://fonts.googleapis.com/css2?family=Open+Sans:wght@400;600;700&display=swap" rel="stylesheet">
<style>
  :root {
    --page: #e9eaee;
    --card-white: #ffffff;
    --brand-blue: #6b93e2;
    --brand-blue-deep: #3f6fd8;
    --brand-blue-light: #e6eeff;
    --brand-taupe: #6e665e;
    --ink: #2f2f2f;
    --on-blue: #ffffff;
  }
  * { box-sizing: border-box; margin: 0; padding: 0; }
  html, body { width: 1200px; height: 980px; overflow: hidden; }
  body {
    background: var(--page);
    font-family: "Open Sans", Arial, sans-serif;
    display: flex;
    flex-direction: column;
    align-items: center;
    justify-content: center;
    gap: 40px;
  }
  .card {
    position: relative;
    width: 760px;
    height: 434px;
    border-radius: 30px;
    overflow: hidden;
    box-shadow: 0 6px 18px rgba(0,0,0,0.12);
  }
  .card-front { background: var(--card-white); }
  .card-front .wave { position: absolute; inset: 0; width: 100%; height: 100%; }

  .brand {
    position: absolute;
    display: flex;
    align-items: center;
    gap: 14px;
    color: var(--brand-taupe);
    font-weight: 400;
  }
  .brand-dot {
    display: block;
    border-radius: 50%;
    background: var(--brand-blue-deep);
  }
  .card-front .brand { left: 70px; top: 62px; font-size: 46px; letter-spacing: 0.5px; }
  .card-front .brand-dot { width: 30px; height: 30px; }

  .person {
    position: absolute;
    left: 72px;
    top: 150px;
    font-size: 26px;
  }
  .person-name { color: var(--brand-blue-deep); font-weight: 700; }
  .person-title { color: var(--ink); font-size: 20px; font-weight: 400; margin-left: 6px; }

  .contacts {
    position: absolute;
    bottom: 26px;
    display: flex;
    flex-direction: column;
    gap: 6px;
    color: var(--on-blue);
    font-size: 19px;
    font-weight: 600;
    list-style: none;
  }
  .contacts-online { left: 270px; bottom: 34px; }
  .contacts-phone { right: 44px; }
  .contacts li { display: flex; align-items: center; gap: 10px; }
  .contacts svg { width: 18px; height: 18px; flex: none; }

  .card-back {
    background: radial-gradient(ellipse 60% 70% at 58% 45%, var(--brand-blue-light) 0%, #a9c0f0 35%, var(--brand-blue) 75%);
  }
  .card-back .brand {
    left: 50%;
    top: 44%;
    transform: translate(-50%, -50%);
    font-size: 54px;
    white-space: nowrap;
  }
  .card-back .brand-dot { width: 36px; height: 36px; }
  .back-web {
    position: absolute;
    left: 60px;
    bottom: 48px;
    color: var(--on-blue);
    font-size: 20px;
    letter-spacing: 5px;
  }
</style>
</head>
<body>

<section class="card card-front" aria-label="Card front">
  <svg class="wave" viewBox="0 0 760 434" preserveAspectRatio="none" aria-hidden="true">
    <path d="M0,212 C120,320 380,352 760,318 L760,434 L0,434 Z" fill="var(--brand-blue)"/>
    <path d="M0,168 C100,272 330,324 560,334 C340,316 120,268 0,196 Z" fill="var(--brand-taupe)"/>
  </svg>

  <div class="brand"><span class="brand-dot"></span>RT Code Transit</div>

  <p class="person"><span class="person-name">Your Name,</span><span class="person-title">Title</span></p>

  <ul class="contacts contacts-online">
    <li>
      <svg viewBox="0 0 20 20" aria-hidden="true"><rect x="2" y="4" width="16" height="12" rx="2" fill="none" stroke="currentColor" stroke-width="2"/><path d="M3,5 L10,11 L17,5" fill="none" stroke="currentColor" stroke-width="2"/></svg>
      info@rtcodetransit.example
    </li>
    <li>
      <svg viewBox="0 0 20 20" aria-hidden="true"><circle cx="10" cy="10" r="8" fill="none" stroke="currentColor" stroke-width="1.8"/><ellipse cx="10" cy="10" rx="3.5" ry="8" fill="none" stroke="currentColor" stroke-width="1.5"/><path d="M2,10 H18 M4,6 H16 M4,14 H16" stroke="currentColor" stroke-width="1.3"/></svg>
      www.rtcodetransit.example
    </li>
  </ul>

  <ul class="contacts contacts-phone">
    <li>
      <svg viewBox="0 0 20 20" aria-hidden="true"><path d="M5,2 L8,2 L9,6 L7,8 C8,11 9,12 12,13 L14,11 L18,12 L18,15 C18,17 16,18 14,18 C8,17 3,12 2,6 C2,4 3,2 5,2 Z" fill="currentColor"/></svg>
      0100 200300
    </li>
    <li>
      <svg viewBox="0 0 20 20" aria-hidden="true"><rect x="5" y="1" width="10" height="18" rx="2" fill="none" stroke="currentColor" stroke-width="2"/><circle cx="10" cy="15.5" r="1.3" fill="currentColor"/></svg>
      0100 200301
    </li>
    <li>
      <svg viewBox="0 0 20 20" aria-hidden="true"><rect x="5" y="2" width="10" height="6" fill="none" stroke="currentColor" stroke-width="1.8"/><rect x="2" y="8" width="16" height="9" rx="2" fill="currentColor"/><rect x="5" y="11" width="10" height="2" fill="var(--brand-blue)"/></svg>
      0100 200302
    </li>
  </ul>
</section>

<section class="card card-back" aria-label="Card back">
  <div class="brand"><span class="brand-dot"></span>RT Code Transit</div>
  <p class="back-web">www.rtcodetransit.example</p>
</section>

</body>
</html>
```